We need a Word Template for Custom Laboratory Results from an independent laboratory

The test is a novel biomarker for a chronic pain condition called endometriosis. It is expressed as a percentage. We will upload a sample result. We are looking for improved graphic fidelity with more attention to design and spacing. Emphasis should be placed on the overall result, i.e. the patient percentage results. Considerationis going to be given to the most appealing graphic result.

Target Market(s)

Women aged 19-45

Colors
0054AA
0677BA
7BADD7
CADEEF
E8F1F8

```html
<!DOCTYPE html>
<html lang="en">
<head>
<meta charset="utf-8">
<title>EndoSignal Micro-RNA Endometriosis Assay – Result Report</title>
<link href="https://fonts.googleapis.com/css2?family=Montserrat:wght@300;400;500;600;700&display=swap" rel="stylesheet">
<style>
  :root {
    --brand-navy: #0054AA;
    --brand-blue: #0677BA;
    --brand-sky: #7BADD7;
    --brand-mist: #CADEEF;
    --brand-ice: #E8F1F8;
    --ink: #6f7478;
    --ink-strong: #54595d;
    --rule: #d9dde0;
    --paper: #ffffff;
    --backdrop: #c9cbcd;
  }
  * { box-sizing: border-box; margin: 0; padding: 0; }
  html, body {
    width: 1200px;
    height: 960px;
    overflow: hidden;
    background: var(--backdrop);
    font-family: "Montserrat", Arial, sans-serif;
  }
  .report {
    position: absolute;
    left: 250px;
    top: 20px;
    width: 700px;
    height: 920px;
    background: var(--paper);
    padding: 44px 52px;
    box-shadow: 0 6px 24px rgba(0,0,0,0.15);
  }
  .report-header {
    display: flex;
    justify-content: space-between;
    align-items: flex-start;
  }
  .clinic-brand {
    display: flex;
    align-items: center;
    gap: 10px;
  }
  .clinic-dot {
    width: 34px;
    height: 34px;
    border-radius: 50%;
    background: var(--brand-sky);
  }
  .clinic-name {
    font-size: 15px;
    font-weight: 600;
    color: var(--ink-strong);
    letter-spacing: 0.02em;
  }
  .lab-name {
    margin-top: 70px;
    font-size: 17px;
    font-weight: 700;
    color: var(--brand-navy);
  }
  .assay-title {
    margin-top: 18px;
    font-size: 34px;
    font-weight: 300;
    line-height: 1.12;
    letter-spacing: 0.04em;
    color: var(--brand-sky);
    text-transform: uppercase;
  }
  .patient-block { margin-top: 36px; }
  .section-label {
    display: inline-block;
    font-size: 12px;
    font-weight: 700;
    color: var(--ink);
    letter-spacing: 0.08em;
    padding-bottom: 8px;
    border-bottom: 1px solid var(--ink);
    width: 200px;
  }
  .patient-fields { list-style: none; margin-top: 8px; }
  .patient-field {
    background: var(--brand-mist);
    opacity: 0.75;
    font-size: 10px;
    color: var(--ink);
    padding: 4px 6px;
    margin-bottom: 6px;
    margin-right: -52px;
  }
  .result-panel {
    margin-top: 26px;
    display: flex;
    border: 1px solid var(--rule);
    min-height: 200px;
  }
  .result-label {
    flex: 1;
    padding: 22px 24px;
    font-size: 13px;
    line-height: 1.45;
    color: var(--ink);
  }
  .result-value {
    width: 290px;
    background: var(--brand-mist);
    opacity: 0.85;
    display: flex;
    align-items: center;
    justify-content: center;
    font-size: 48px;
    font-weight: 300;
    color: var(--brand-blue);
    letter-spacing: 0.02em;
  }
  .reference {
    margin-top: 30px;
    font-size: 11px;
    color: var(--ink);
    line-height: 1.6;
  }
  .reference-title {
    font-weight: 700;
    color: var(--ink-strong);
    margin-bottom: 2px;
  }
  .reference-list { list-style: none; padding-left: 14px; }
</style>
</head>
<body>
  <main class="report">
    <header class="report-header">
      <div class="clinic-brand">
        <span class="clinic-dot"></span>
        <span class="clinic-name">Meridian Fertility Centre</span>
      </div>
      <div class="lab-name">Lumora Labs</div>
    </header>

    <h1 class="assay-title">EndoSignal Micro-RNA<br>Endometriosis Assay</h1>

    <section class="patient-block">
      <h2 class="section-label">YOUR RESULTS</h2>
      <ul class="patient-fields">
        <li class="patient-field">[Last Name], [First Name]</li>
        <li class="patient-field">[OHIP Number (12 characters)]</li>
        <li class="patient-field">[DOB]</li>
      </ul>
    </section>

    <section class="result-panel">
      <p class="result-label">Predicted Probability of Endometriosis Compared to Surgical Controls (100% probability)</p>
      <div class="result-value">38.7%</div>
    </section>

    <section class="reference">
      <h3 class="reference-title">Reference Range</h3>
      <ol class="reference-list">
        <li>1. 0.0–29.9% - low probability of endometriosis</li>
        <li>2. 29.9–44.9% - inconclusive</li>
        <li>3. 45.0–55.0% - intermediate risk of endometriosis</li>
        <li>4. 55.1–64.9% - probable endometriosis</li>
        <li>5. 65.0–99.9% - highly probable endometriosis</li>
      </ol>
    </section>
  </main>
</body>
</html>
```